Powerpoint Presentation

We have a basic 8 page presentation that we would like created on powerpoint. The presentation is very simple dot points and we would like to jazz it up with relevant photos/images relating to the topic on each page.

The topic of the presentation is 'creating a powerful presence and knowing your personal brand' (see attached files).

Target Market(s)

Business women

Requirements
Must have
• Images that match the content on each page

```html
<!DOCTYPE html>
<html lang="en">
<head>
<meta charset="utf-8">
<title>Presence and Personal Brand – Slide Deck</title>
<link rel="stylesheet" href="https://fonts.googleapis.com/css2?family=Arimo:ital,wght@0,400;0,700;1,400;1,700&family=Archivo:wght@800;900&display=swap">
<style>
  :root {
    --red: #ee1c1c;
    --orange: #f0752b;
    --ink: #1a1a1a;
    --grey: #666666;
    --sky-deep: #2f7fe6;
    --sky-mid: #6fb2f5;
    --sky-pale: #dcecfc;
    --page: #ffffff;
    --slide-shadow: rgba(0,0,0,0.28);
  }
  * { box-sizing: border-box; margin: 0; padding: 0; }
  html, body { width: 1200px; height: 1028px; overflow: hidden; background: var(--page); }
  body { position: relative; font-family: "Arimo", Arial, sans-serif; color: var(--ink); }

  .slide-number {
    position: absolute; width: 366px; text-align: center;
    font-size: 24px; color: var(--red); line-height: 1;
  }
  .slide {
    position: absolute; width: 366px; height: 274px; overflow: hidden;
    background: var(--page);
    box-shadow: 0 1px 4px var(--slide-shadow);
  }
  .slide::before {
    content: ""; position: absolute; left: 0; right: 0; top: 0; height: 36px;
    background: linear-gradient(180deg, var(--sky-deep) 0%, var(--sky-mid) 45%, var(--sky-pale) 80%, rgba(255,255,255,0) 100%);
  }
  .col-1 { left: 37px; } .col-2 { left: 418px; } .col-3 { left: 797px; }
  .row-1 { top: 65px; } .row-2 { top: 389px; } .row-3 { top: 718px; }
  .num.row-1 { top: 30px; } .num.row-2 { top: 356px; } .num.row-3 { top: 686px; }

  .brand-mark { position: absolute; left: 9px; bottom: 30px; width: 20px; height: 20px; background: var(--orange); border-radius: 3px; }
  .brand-name { position: absolute; left: 9px; bottom: 11px; font-size: 11px; color: var(--orange); white-space: nowrap; }

  .photo { position: absolute; border-radius: 8px; }

  .title {
    position: absolute; font-family: "Archivo", "Arimo", sans-serif; font-weight: 900;
    color: var(--red); text-decoration: underline; text-decoration-thickness: 2px;
    text-underline-offset: 3px; line-height: 1.12; letter-spacing: -0.3px; white-space: nowrap;
  }

  /* Slide 1 – cover */
  .cover { background: radial-gradient(ellipse at 50% 60%, #f4f9ff 0%, #9cc8f6 38%, var(--sky-deep) 100%); }
  .cover::before { display: none; }
  .cover-mark { position: absolute; left: 155px; top: 94px; width: 56px; height: 56px; background: var(--orange); border-radius: 6px; }
  .cover-name { position: absolute; left: 0; right: 0; top: 160px; text-align: center; font-size: 25px; color: var(--orange); }

  /* Slide 2 – agenda */
  .agenda { position: absolute; left: 0; right: 0; top: 58px; text-align: center; color: var(--red); font-size: 30px; line-height: 40px; }

  /* Slide 3 */
  .s3-title { left: 0; right: 0; top: 14px; text-align: center; font-family: "Arimo", sans-serif; font-weight: 400; font-size: 30px; letter-spacing: -0.5px; }
  .s3-title b { font-weight: 700; }
  .s3-points { position: absolute; left: 6px; width: 216px; top: 106px; text-align: center; font-weight: 700; font-size: 14.5px; line-height: 1.25; letter-spacing: -0.2px; }
  .s3-points p { margin-bottom: 11px; }

  /* Slide 4 */
  .s4-title { left: 0; right: 0; top: 34px; text-align: center; font-size: 30px; }
  .s4-quote { position: absolute; left: 48px; right: 48px; top: 96px; text-align: center; font-style: italic; font-size: 21px; line-height: 1.25; }

  /* Slide 5 */
  .s5-title { left: 18px; top: 50px; font-size: 28px; }
  .s5-badge { position: absolute; left: 124px; top: 92px; width: 34px; height: 34px; border-radius: 50%; background: #8a8f98; }
  .s5-value { position: absolute; left: 18px; top: 134px; font-size: 21px; letter-spacing: -0.6px; }
  .s5-value b { color: var(--red); }
  .s5-list { position: absolute; left: 18px; top: 166px; list-style: none; font-style: italic; color: var(--grey); font-size: 13px; line-height: 1.5; }
  .s5-list li::before { content: "➢ "; font-style: normal; color: #555; }
  .s5-square { position: absolute; left: 212px; top: 234px; width: 40px; height: 18px; background: #9aa0a8; }

  /* Slide 6 */
  .s6-title { left: 18px; top: 52px; font-size: 28px; }
  .s6-q { position: absolute; left: 16px; top: 146px; font-style: italic; font-size: 20px; line-height: 1.32; letter-spacing: -0.4px; }
  .s6-q b { color: var(--red); }

  /* Slide 7 */
  .s7-title { left: 14px; top: 84px; font-size: 27px; }
  .s7-lines { position: absolute; left: 14px; top: 120px; font-size: 21px; line-height: 28px; letter-spacing: -0.8px; }
  .s7-lines em { color: var(--red); font-weight: 700; }

  /* Slide 8 */
  .s8-title { left: 16px; top: 60px; font-size: 28px; }
  .s8-lines { position: absolute; left: 16px; top: 144px; font-size: 19.5px; line-height: 1.33; letter-spacing: -0.5px; }
  .s8-note { position: absolute; right: 16px; top: 200px; font-size: 11px; font-style: italic; color: var(--grey); }

  /* Slide 9 */
  .summary { position: absolute; left: 0; right: 0; top: 50px; text-align: center; color: var(--red); font-family: "Archivo", "Arimo", sans-serif; font-weight: 800; font-size: 21px; line-height: 30px; letter-spacing: -0.3px; }
</style>
</head>
<body>

<div class="slide-number num col-1 row-1">1</div>
<div class="slide-number num col-2 row-1">2</div>
<div class="slide-number num col-3 row-1">3</div>
<div class="slide-number num col-1 row-2">4</div>
<div class="slide-number num col-2 row-2">5</div>
<div class="slide-number num col-3 row-2">6</div>
<div class="slide-number num col-1 row-3">7</div>
<div class="slide-number num col-2 row-3">8</div>
<div class="slide-number num col-3 row-3">9</div>

<!-- 1 Cover -->
<section class="slide cover col-1 row-1">
  <div class="cover-mark"></div>
  <div class="cover-name">quiet room coaching</div>
</section>

<!-- 2 Agenda -->
<section class="slide col-2 row-1">
  <div class="agenda">Presence<br>Positioning<br>Voice and Language</div>
  <div class="brand-mark"></div><div class="brand-name">quiet room coaching</div>
</section>

<!-- 3 Powerful presence -->
<section class="slide col-3 row-1">
  <h2 class="title s3-title">Create a <b>powerful</b><br><b>presence</b> by:</h2>
  <div class="s3-points">
    <p>Knowing your personal brand</p>
    <p>Building and maintaining relationships-networking</p>
    <p>Elevator pitch</p>
  </div>
  <div class="photo" role="img" aria-label="Person with open arms against a bright sky" style="left:228px; top:112px; width:126px; height:95px; background: radial-gradient(ellipse at 50% 35%, #eef6fb 0%, #8fb7cf 45%, #4d6f86 100%);"></div>
  <div class="brand-mark"></div><div class="brand-name">quiet room coaching</div>
</section>

<!-- 4 What is presence -->
<section class="slide col-1 row-2">
  <h2 class="title s4-title">What is Presence?</h2>
  <p class="s4-quote">"The state of being present in a situation or with a person"</p>
  <div role="img" aria-label="Illustration of many colourful raised hands" style="position:absolute; left:132px; top:194px; width:220px; height:80px; background: linear-gradient(90deg, #f5a623 0%, #e94b8a 25%, #5ac8e8 50%, #7cc243 75%, #f25c3c 100%); opacity:0.85; border-radius: 40px 40px 0 0;"></div>
  <div class="brand-mark"></div><div class="brand-name">quiet room coaching</div>
</section>

<!-- 5 Personal brand -->
<section class="slide col-2 row-2">
  <h2 class="title s5-title">Personal<br>Brand</h2>
  <div class="s5-badge"></div>
  <p class="s5-value">Know <b>your</b> value</p>
  <ul class="s5-list">
    <li>How do you see yourself?</li>
    <li>How do others see you?</li>
  </ul>
  <div class="photo" role="img" aria-label="Portrait of a pop singer with pink hair" style="left:168px; top:40px; width:86px; height:96px; background: linear-gradient(135deg, #f08a9a 0%, #d94f6a 50%, #3c2a36 100%);"></div>
  <div class="photo" role="img" aria-label="Fashion portrait of a man in a dark suit" style="left:262px; top:40px; width:96px; height:96px; background: linear-gradient(160deg, #4a4a4a 0%, #1e1e1e 100%);"></div>
  <div class="photo" role="img" aria-label="Portrait of a business executive at a corporate event" style="left:212px; top:142px; width:146px; height:86px; background: linear-gradient(135deg, #b73a3a 0%, #e6c9b8 55%, #7a2a2a 100%);"></div>
  <div class="s5-square"></div>
  <div class="brand-mark"></div><div class="brand-name">quiet room coaching</div>
</section>

<!-- 6 Elevator pitch -->
<section class="slide col-3 row-2">
  <h2 class="title s6-title">Elevator<br>Pitch</h2>
  <div class="photo" role="img" aria-label="Business colleagues talking in an office" style="left:176px; top:29px; width:174px; height:110px; background: linear-gradient(135deg, #e9edf1 0%, #9aa7b3 45%, #3e4650 100%);"></div>
  <p class="s6-q">What do you do?<br>What is <b>your</b> value proposition?</p>
  <div class="brand-mark"></div><div class="brand-name">quiet room coaching</div>
</section>

<!-- 7 Networking -->
<section class="slide col-1 row-3">
  <div role="img" aria-label="Small group of people icons passing messages" style="position:absolute; left:148px; top:38px; width:72px; height:44px; background: linear-gradient(135deg, #f2c14e, #6cc04a, #4aa3df); border-radius:6px; opacity:0.8;"></div>
  <div role="img" aria-label="Network diagram of connected people icons" style="position:absolute; left:242px; top:58px; width:114px; height:84px; border-radius:40px; background: radial-gradient(ellipse at 50% 50%, #f3e2ec 0%, #d8a8c4 60%, rgba(255,255,255,0) 100%);"></div>
  <h2 class="title s7-title">Networking</h2>
  <p class="s7-lines"><em>Invest time</em> in your career<br><em>Make</em> the time</p>
  <div role="img" aria-label="Row of business people shaking hands" style="position:absolute; left:160px; top:180px; width:190px; height:84px; background: linear-gradient(180deg, #d8d8d8 0%, #5a5a5a 60%, #2b2b2b 100%); border-radius:6px; opacity:0.85;"></div>
  <div class="brand-mark"></div><div class="brand-name">quiet room coaching</div>
</section>

<!-- 8 Voice and language -->
<section class="slide col-2 row-3">
  <h2 class="title s8-title">Voice and<br>Language</h2>
  <div class="photo" role="img" aria-label="Portrait of a woman politician speaking" style="left:186px; top:46px; width:70px; height:90px; background: linear-gradient(135deg, #d9c7a8 0%, #8f7b5e 100%);"></div>
  <div class="photo" role="img" aria-label="Woman speaking in parliament" style="left:266px; top:68px; width:84px; height:72px; background: linear-gradient(135deg, #7aa0c8 0%, #2f4a78 100%);"></div>
  <p class="s8-lines">Get your message across<br>Least amount of negative language</p>
  <p class="s8-note">(no, never, can’t, don’t)</p>
  <div class="brand-mark"></div><div class="brand-name">quiet room coaching</div>
</section>

<!-- 9 Summary -->
<section class="slide col-3 row-3">
  <div class="summary">Presence<br>Personal Brand<br>Elevator Pitches<br>Relationship building-networking<br>Voice and language</div>
  <div class="brand-mark"></div><div class="brand-name">quiet room coaching</div>
</section>

</body>
</html>
```